Etiketten für Kuchen im Glas
Zielgruppe
Die Firma Brelkat bietet kulinarische Präsente und Geschenkideen zum Thema kreatives Backen an. Unsere Zielgruppe ist B2C und Werbetreibende, die unsere Produkte als Geschenke einsetzen.
Aufgabenstellung
Für unsere Zielgruppe "Feinkostläden" benötigen wir ein etwas edleres klasssisches Etiketten-Design.
Gestaltet wird der Deckel und die Vorderseite eines Etiketts für ein 290 ml FUMS-Glas. Die entsprechende Designvorlage steht hier zum Download bereit:
https://files.tralvex-speicher.de/u/4827351/7902_01358_0000-Vorlage%20CMYK%20v08_2013-09.psd
Benötigt werden 4 unterschiedliche Etiketten, die aber aus einem "Guss" sein sollten für die Sorten: Stracciatella, Schokolade, Zitrone, Stollen. Die Sorte sollte mit auf dem Etikett stehen.
Sonstige Angaben auf dem Etikett:
- optional "Kuchen im Glas"
- gerne Grünhof Logo (siehe Anhang)
- optional "fertig gebacken". Könnte z.B. gut auf dem Deckel in Kombination mit "Kuchen im Gla" stehen
Achtung: Das Etikett für die Rückseite mit Deklaration muss nicht gestaltet werden.
Tipps: Das Etikett ist konisch und das Glas rund. Das bedeutet, dass Bilder + Schriften mit einer leichten Wölbung kreiert werden sollten. Für die Wölbung kann man sich gut an der unteren Designlinie orientieren.
Farbgestaltung: eher dunkel; z.B. Grau, Dunkelblau evtl. Schwarz
Schriften: Es dürfen auch kostenpflichtige Schriften verwendet werden. Freie Schriften allerdings bevorzugt
Format: Photoshop PSD inklusive allen Ebenen und verwendeten Elementen als einzelne Ebene.
Bei Fragen gerne melden, ich freue mich auf Eure Designs.

```html
<!DOCTYPE html>
<html lang="de">
<head>
<meta charset="utf-8">
<title>Kuchen im Glas – Zitrone Etiketten</title>
<link rel="stylesheet" href="https://fonts.googleapis.com/css2?family=Limelight&family=Cormorant+Garamond:wght@500&family=Italiana&display=swap">
<style>
  :root {
    --label-yellow: #fdc800;
    --band-yellow: #f5c400;
    --band-fade: #3a2e00;
    --label-black: #111110;
    --pattern-grey: #2b2a26;
    --title-cream: #fdead0;
    --script-white: #f6f3ec;
    --variety-ink: #1a1608;
    --drawing-tone: #d9d6cd;
    --page: #ffffff;
  }
  html, body {
    margin: 0;
    padding: 0;
    width: 1200px;
    height: 386px;
    overflow: hidden;
    background: var(--page);
  }
  .labels { display: block; width: 1200px; height: 386px; }
  .label-title {
    font-family: "Limelight", "Italiana", serif;
    fill: var(--title-cream);
  }
  .variety-name {
    font-family: "Italiana", "Limelight", serif;
    fill: var(--variety-ink);
    font-weight: 700;
  }
  .baked-note {
    font-family: "Cormorant Garamond", serif;
    font-weight: 500;
    fill: var(--script-white);
  }
  .farm-name {
    font-family: "Cormorant Garamond", serif;
    font-weight: 500;
    fill: var(--script-white);
  }
  .farm-dot { fill: var(--script-white); }
</style>
</head>
<body>
<svg class="labels" viewBox="0 0 1200 386" xmlns="http://www.w3.org/2000/svg">
  <defs>
    <radialGradient id="pattern-tone" cx="50%" cy="45%" r="70%">
      <stop offset="0" stop-color="var(--pattern-grey)"/>
      <stop offset="1" stop-color="var(--label-black)"/>
    </radialGradient>
    <linearGradient id="variety-band" x1="0" x2="1" y1="0" y2="0">
      <stop offset="0" stop-color="var(--band-fade)" stop-opacity="0.2"/>
      <stop offset="0.2" stop-color="var(--band-yellow)"/>
      <stop offset="0.8" stop-color="var(--band-yellow)"/>
      <stop offset="1" stop-color="var(--band-fade)" stop-opacity="0.2"/>
    </linearGradient>
    <path id="lid-baked-arc" d="M77,289 A150,150 0 0 0 307,289"/>
    <path id="front-baked-curve" d="M690,304 Q850,290 1015,306"/>
  </defs>

  <g class="lid-label">
    <circle cx="192" cy="193" r="187" fill="var(--label-yellow)"/>
    <circle cx="192" cy="193" r="171" fill="url(#pattern-tone)" role="img" aria-label="Dunkles florales Ornamentmuster"/>
    <text class="label-title" x="65" y="171" font-size="50" textLength="261" lengthAdjust="spacingAndGlyphs">Kuchen im Glas</text>
    <rect x="90" y="182" width="204" height="19" fill="url(#variety-band)"/>
    <text class="variety-name" x="137" y="198" font-size="18" textLength="121" lengthAdjust="spacing">ZITRONE</text>
    <ellipse cx="188" cy="302" rx="35" ry="22" fill="var(--drawing-tone)" opacity="0.85" role="img" aria-label="Gezeichnete Zitrone mit Zitronenscheibe"/>
    <text class="baked-note" font-size="22">
      <textPath href="#lid-baked-arc" textLength="256" lengthAdjust="spacing">Fertig  gebacken</textPath>
    </text>
  </g>

  <g class="front-label">
    <path d="M450,37 Q823,-21 1196,53 L1140,366 Q822,284 503,373 Z" fill="var(--label-yellow)"/>
    <path d="M470,49 Q823,0 1177,67 L1130,347 Q823,293 516,351 Z" fill="url(#pattern-tone)" role="img" aria-label="Dunkles florales Ornamentmuster"/>
    <text class="label-title" x="618" y="162" font-size="92" textLength="423" lengthAdjust="spacingAndGlyphs">Kuchen im Glas</text>
    <rect x="678" y="179" width="288" height="28" fill="url(#variety-band)"/>
    <text class="variety-name" x="744" y="203" font-size="27" textLength="174" lengthAdjust="spacing">ZITRONE</text>
    <ellipse cx="830" cy="275" rx="50" ry="32" fill="var(--drawing-tone)" opacity="0.85" role="img" aria-label="Gezeichnete Zitrone mit Zitronenscheibe"/>
    <g class="farm-mark">
      <circle class="farm-dot" cx="656" cy="288" r="7"/>
      <text class="farm-name" x="656" y="313" font-size="15" text-anchor="middle">Grünhof</text>
    </g>
    <text class="baked-note" font-size="22" letter-spacing="7">
      <textPath href="#front-baked-curve" startOffset="10">Fertig</textPath>
    </text>
    <text class="baked-note" font-size="22" letter-spacing="7">
      <textPath href="#front-baked-curve" startOffset="190">gebacken</textPath>
    </text>
  </g>
</svg>
</body>
</html>
```